Tallis Ecological Works New Website Design

I need a new website for a Environmental Project Company based in Sydney Australia, working throughout South East Asia.I've attached the company logo, please try & incorporate these colours or use complimentary colours. I've attached a word doc with design brief.I'm going to use Wix, so please ensure files are suitable.Thankyou.

Number of Pages Required

5+ page

Colors

Designer to choose colors to be used in the design.

Requirements
Must have
• Refer to Word Document
Nice to have
• Refer to Word Document
Should not have
• Not to be dark

```html
<!DOCTYPE html>
<html lang="en">
<head>
<meta charset="utf-8">
<title>Tallis Ecological Works</title>
<link href="https://fonts.googleapis.com/css2?family=Playfair+Display:wght@400;700&family=Lato:wght@400;700&display=swap" rel="stylesheet">
<style>
:root{
  --olive:#4b6a28;
  --forest:#3e5a24;
  --forest-deep:#24351a;
  --ink:#1d2a17;
  --text:#5b5f58;
  --muted:#8b8f88;
  --line:#d8dbd5;
  --mist:#eef0ed;
  --white:#ffffff;
  --leaf:#9bc46a;
  --serif:'Playfair Display', Georgia, serif;
  --sans:'Lato', Arial, sans-serif;
}
*{box-sizing:border-box;margin:0;padding:0}
html,body{width:1200px;height:3846px;overflow:hidden;background:var(--white)}
body{position:relative;font-family:var(--sans);color:var(--text)}
.abs{position:absolute}

/* header */
.site-header{position:absolute;left:0;top:0;width:1200px;height:140px}
.main-nav{position:absolute;left:118px;top:44px;display:flex;gap:16px;font-size:11px;color:var(--ink)}
.brand{position:absolute;display:flex;align-items:center;gap:12px}
.brand-dot{width:40px;height:40px;border-radius:50%;background:var(--forest)}
.brand-name{font-family:var(--serif);font-weight:700;color:var(--forest);font-size:20px;line-height:1.1;letter-spacing:1px;text-transform:uppercase}
.header-brand{left:508px;top:40px}
.header-contact{position:absolute;right:26px;top:44px;font-size:11px;color:var(--ink)}
.header-contact b{font-weight:700}

.eyebrow{font-size:12px;letter-spacing:4px;text-transform:uppercase;text-align:center}

/* vision */
.vision{position:absolute;top:140px;left:0;width:1200px;height:283px}
.vision .eyebrow{position:absolute;top:16px;width:100%;color:var(--olive)}
.vision-text{position:absolute;top:42px;left:360px;width:480px;text-align:center;font-family:var(--serif);font-size:25px;line-height:35px;color:var(--olive)}

/* mission */
.mission{position:absolute;top:423px;left:0;width:1200px;height:731px;background:var(--forest)}
.mission .eyebrow{position:absolute;top:80px;width:100%;color:#dfe8d4}
.mission-text{position:absolute;top:108px;left:370px;width:460px;text-align:center;font-family:var(--serif);font-size:25px;line-height:34px;color:var(--white)}
.focus{position:absolute;left:197px;top:365px;color:var(--white)}
.focus-intro{font-size:13px;margin-bottom:16px}
.focus-list{list-style:none;font-family:var(--serif);font-size:17px;line-height:32px}
.focus-list li{display:flex;align-items:center;gap:10px}
.focus-list li::before{content:"";width:6px;height:6px;background:var(--leaf)}
.mission-photo{position:absolute;left:600px;top:308px;width:400px;height:341px;background:linear-gradient(160deg,#8fb35a 0%,#c9d6a8 45%,#e7d3bd 70%,#6e7d3a 100%)}

/* products */
.products-band{position:absolute;top:1154px;left:0;width:1200px;height:148px;background:var(--forest-deep)}
.products-band h2{position:absolute;top:60px;width:100%;text-align:center;font-family:var(--serif);font-weight:400;font-size:28px;letter-spacing:7px;color:var(--white)}
.product-grid{position:absolute;top:1302px;left:0;width:1200px;height:703px;display:grid;grid-template-columns:repeat(4,300px);grid-template-rows:repeat(3,234px);gap:1px;background:#1a2513}
.tile{position:relative;display:flex;align-items:center;justify-content:center}
.tile span{font-size:15px;font-weight:700;color:var(--white);text-align:center;text-transform:uppercase;line-height:18px;width:150px;text-shadow:0 1px 3px rgba(0,0,0,.35)}
.tile.active{background:#2f4424!important}
.tile.active span{text-shadow:none;padding-bottom:12px;border-bottom:3px solid #5fae3e}

/* news */
.news{position:absolute;top:2005px;left:0;width:1200px;height:880px}
.news .eyebrow{position:absolute;top:76px;width:100%;color:var(--muted)}
.news-photo{position:absolute;width:388px;height:234px}
.post{position:absolute;width:386px}
.post-meta{display:flex;align-items:center;gap:6px;font-size:8px;color:var(--muted);line-height:10px}
.avatar{width:16px;height:16px;border-radius:50%;background:#b8bcb5}
.post h3{font-family:var(--serif);font-weight:400;font-size:20px;color:var(--olive);margin:8px 0 6px}
.post p{font-size:8.5px;line-height:13px;color:var(--text)}
.post-foot{margin-top:12px;padding-top:8px;border-top:1px solid var(--line);font-size:8px;color:var(--muted);display:flex;gap:14px}

/* contact */
.contact{position:absolute;top:2885px;left:0;width:1200px;height:687px;background:var(--mist)}
.contact .eyebrow{position:absolute;top:84px;width:100%;color:var(--muted)}
.contact h2{position:absolute;top:182px;width:100%;text-align:center;font-family:var(--serif);font-weight:400;font-size:27px;color:var(--olive)}
.field-label{position:absolute;top:282px;font-size:10px;color:var(--ink)}
.field{position:absolute;height:35px;background:var(--white);border:1px solid var(--line);font-size:10px;color:var(--text);padding:0 12px;display:flex;align-items:center}
.select{justify-content:space-between}
.textarea{align-items:flex-start;padding-top:12px}
.submit{position:absolute;left:541px;top:574px;width:118px;height:33px;background:var(--ink);color:var(--white);font-size:10px;font-weight:700;letter-spacing:3px;display:flex;align-items:center;justify-content:center}

/* footer */
.site-footer{position:absolute;top:3572px;left:0;width:1200px;height:274px}
.tagline{position:absolute;left:118px;top:72px;font-family:var(--serif);font-size:27px;color:var(--olive)}
.footer-brand{left:490px;top:64px}
.footer-contact{position:absolute;right:26px;top:82px;display:flex;gap:20px;font-size:11px;color:var(--ink);align-items:center}
.footer-contact span{display:flex;align-items:center;gap:6px}
.copyright{position:absolute;top:186px;width:100%;text-align:center;font-size:10px;line-height:16px;color:var(--text)}
</style>
</head>
<body>

<header class="site-header">
  <nav class="main-nav"><span>Home</span><span>Who we are</span><span>Services</span><span>Products</span><span>News</span><span>Contact</span></nav>
  <div class="brand header-brand"><div class="brand-dot"></div><div class="brand-name">Tallis<br>Ecological Works</div></div>
  <div class="header-contact"><b>Phone:</b> +00 000 0000 &nbsp;|&nbsp; <b>Email:</b> info@tallisworks.au</div>
</header>

<section class="vision">
  <p class="eyebrow">Vision Statement</p>
  <p class="vision-text">Our Vision is to make it easy for everyone to minimise their environmental impact by providing information, technology, packaged green solutions &amp; helping innovation flourish.</p>
</section>

<section class="mission">
  <p class="eyebrow">Mission Statement</p>
  <p class="mission-text">Working with people to minimise the environmental impact of humans on the earth without sacrificing lifestyle and helping innovation flourish.</p>
  <div class="focus">
    <p class="focus-intro">We will achieve this by focusing on the following:</p>
    <ul class="focus-list">
      <li>Sustainable food.</li>
      <li>Sustainable / Renewable power.</li>
      <li>Water quality &amp; treatment.</li>
      <li>Air quality.</li>
      <li>Investing in green infrastructure &amp; projects.</li>
      <li>Education.</li>
    </ul>
  </div>
  <div class="mission-photo" role="img" aria-label="Cupped hands holding a young seedling in soil"></div>
</section>

<section class="products-band"><h2>PRODUCTS &amp; SERVICES</h2></section>
<div class="product-grid">
  <div class="tile" role="img" aria-label="Wind turbines under a blue sky" style="background:linear-gradient(180deg,#3f86c6,#a9cfe8 70%,#5c8a3a)"><span>Simply Dummy Lorem Ipsum</span></div>
  <div class="tile" role="img" aria-label="Hands planting in garden soil" style="background:linear-gradient(160deg,#7a8a4a,#b9a27a 55%,#6b5a3c)"><span>Simply Dummy Lorem Ipsum Printing</span></div>
  <div class="tile" role="img" aria-label="White clouds in a blue sky" style="background:linear-gradient(180deg,#5d8fc4,#d8e4ee 60%,#9ab8d6)"><span>Printing and Typesetting</span></div>
  <div class="tile" role="img" aria-label="Gloved hand sampling water" style="background:linear-gradient(160deg,#8f9fb2,#d7dde4 55%,#6d7f92)"><span>Lorem Ipsum Printing and</span></div>
  <div class="tile" role="img" aria-label="House shape on green grass" style="background:linear-gradient(180deg,#4f9a2e,#8cc84a 60%,#3f7a22)"><span>Simply Dummy Lorem Ipsum</span></div>
  <div class="tile active"><span>Simply Dummy Lorem Ipsum Printing</span></div>
  <div class="tile" role="img" aria-label="Aerial view of highway through fields" style="background:linear-gradient(180deg,#7c9bbb,#6f8a58 50%,#4a6436)"><span>Printing and Typesetting</span></div>
  <div class="tile" role="img" aria-label="Solar panels at sunset" style="background:linear-gradient(180deg,#c7b9d6,#4a5f8f 55%,#2c3a5c)"><span>Lorem Ipsum Printing and</span></div>
  <div class="tile" role="img" aria-label="Child with a drawn light bulb idea" style="background:linear-gradient(160deg,#1f6b5a,#2e8a72 60%,#d9a57e)"><span>Simply Dummy Lorem Ipsum</span></div>
  <div class="tile" role="img" aria-label="Grass field with a house behind" style="background:linear-gradient(180deg,#a9c9e0,#5a7a3a 45%,#3f8a22)"><span>Simply Dummy Lorem Ipsum Printing</span></div>
  <div class="tile" role="img" aria-label="Water droplet splash" style="background:linear-gradient(180deg,#1e3c6e,#3e7db5 55%,#a8c9e4)"><span>Printing and Typesetting</span></div>
  <div class="tile" role="img" aria-label="Park bench among green trees" style="background:linear-gradient(160deg,#4d7a2a,#7ea848 50%,#5b4a30)"><span>Lorem Ipsum Printing and</span></div>
</div>

<section class="news">
  <p class="eyebrow">Our News</p>
  <div class="news-photo" role="img" aria-label="Power transmission towers over a field" style="left:197px;top:162px;background:linear-gradient(180deg,#c9d3dc,#e4e8ec 60%,#6f8a4a 80%,#a85a3a)"></div>
  <article class="post" style="left:615px;top:213px">
    <div class="post-meta"><div class="avatar"></div><div>Admin<br>Dec 19, 2018 · 2 min</div></div>
    <h3>COMING UP</h3>
    <p>Lorem Ipsum has been the industry's standard dummy text ever since the 1500s, when an unknown printer took a galley of type and scrambled it to make a type specimen book. It has survived not only five centuries, but also the leap into electronic typesetting, remaining essentially unchanged.</p>
    <div class="post-foot"><span>0 views</span><span>Write a comment</span></div>
  </article>

  <article class="post" style="left:197px;top:448px">
    <div class="post-meta"><div class="avatar"></div><div>Admin<br>Dec 19, 2018 · 2 min</div></div>
    <h3>COMING UP</h3>
    <p>Lorem Ipsum has been the industry's standard dummy text ever since the 1500s, when an unknown printer took a galley of type and scrambled it to make a type specimen book. It has survived not only five centuries, but also the leap into electronic typesetting, remaining essentially unchanged.</p>
    <div class="post-foot"><span>0 views</span><span>Write a comment</span></div>
  </article>
  <div class="news-photo" role="img" aria-label="Tall green grass close up" style="left:615px;top:396px;background:linear-gradient(180deg,#3f7a1e,#6fae32 50%,#4a8a24)"></div>

  <div class="news-photo" role="img" aria-label="Family sharing a meal at a table" style="left:197px;top:631px;background:linear-gradient(160deg,#c9c2b4,#e8e2d6 45%,#b88a6a 75%,#7a6a58)"></div>
  <article class="post" style="left:615px;top:682px">
    <div class="post-meta"><div class="avatar"></div><div>Admin<br>Dec 19, 2018 · 2 min</div></div>
    <h3>COMING UP</h3>
    <p>Lorem Ipsum has been the industry's standard dummy text ever since the 1500s, when an unknown printer took a galley of type and scrambled it to make a type specimen book. It has survived not only five centuries, but also the leap into electronic typesetting, remaining essentially unchanged.</p>
    <div class="post-foot"><span>0 views</span><span>Write a comment</span></div>
  </article>
</section>

<section class="contact">
  <p class="eyebrow">Contact Us</p>
  <h2>Lorem Ipsum is simply dummy text of the printing and<br>typesetting industry.</h2>
  <span class="field-label" style="left:310px">Name</span>
  <span class="field-label" style="left:508px">Phone</span>
  <span class="field-label" style="left:705px">Email</span>
  <div class="field" style="left:310px;top:300px;width:185px">First Name</div>
  <div class="field" style="left:508px;top:300px;width:185px">+00 000 0000</div>
  <div class="field" style="left:705px;top:300px;width:183px">you@site.com</div>
  <div class="field select" style="left:310px;top:351px;width:578px">Inspection Needed
    <svg width="12" height="8" viewBox="0 0 12 8"><path d="M1 1l5 5 5-5" fill="none" stroke="#1d2a17" stroke-width="1.5"/></svg>
  </div>
  <div class="field textarea" style="left:310px;top:397px;width:578px;height:146px">Message</div>
  <div class="submit">SUBMIT</div>
</section>

<footer class="site-footer">
  <p class="tagline">Available by Phone 24/7!</p>
  <div class="brand footer-brand"><div class="brand-dot"></div><div class="brand-name">Tallis<br>Ecological Works</div></div>
  <div class="footer-contact">
    <span><svg width="14" height="14" viewBox="0 0 24 24"><path d="M6.6 10.8a15 15 0 006.6 6.6l2.2-2.2a1 1 0 011-.25 11 11 0 003.6.6 1 1 0 011 1V20a1 1 0 01-1 1A17 17 0 013 4a1 1 0 011-1h3.5a1 1 0 011 1 11 11 0 00.6 3.6 1 1 0 01-.25 1z" fill="#8b8f88"/></svg><b>Phone:</b> +00 000 0000</span>
    <span><svg width="16" height="12" viewBox="0 0 16 12"><rect x="0.5" y="0.5" width="15" height="11" rx="1.5" fill="#8b8f88"/><path d="M1 1.5l7 5 7-5" fill="none" stroke="#fff" stroke-width="1.2"/></svg><b>Email:</b> info@tallisworks.au</span>
  </div>
  <p class="copyright">© 2019 Tallis Ecological Works. All Rights Reserved.</p>
</footer>

</body>
</html>
```